Salmon Shop that sells both wholesale and retail salmon in a variety of ways.

"Tidewater Fishery" is a business that is selling atlantic salmon in every way possible. We will be a salmon butcher to the public for retail purchase and we will also be out and about trying to sell our products to restaurants cafes and any other wholesale way. Our product is from Tasmania but we will be trading on the Sunshine Coast. The shop design has an urban, rustic feel and very much about the product. One of the owners has worked on salmon farms for 15 years and we want it to be very specialised and quality. I have nothing to offer you to help with this design....I would like both a salmon on the card, not sure if image or silohette is best and would like the other side to have a fillet with a tag of some sort. We are looking for a logo also. Use a photo of an Atlantic Salmon, Atlantic Salmon have two fins along the back.
Updates

Project Deadline Extended Reason: I am extending the deadline as I have still not got exactly what I want. All designers have added something great to what I am after and I just need someone to pull it all together. I have put in a new brief with a sketched image to help so we can get this perfect. Please read all the instructions. Thank you Added Monday, February 16, 2015

Target Market(s)

Restaurants, cafes

Industry/Entity Type

Retail

Contact Information for Business Card

Tidewater Fishery (Not to have "Shop" at the end.Shop 12/130-164 Brisbane RdMooloolaba 4557

Colors
1c66ab

Requirements
Must have
• logo for Tidewater Fishery with the S being salmon fillet of fresh salmon on white platemap of tasmaniasepia /black and white image of atlantic salmon
Nice to have
• fillet of salmonmap of tasmaniasalmon
Should not have
• Not Shop at the end.

```html
<!DOCTYPE html>
<html lang="en">
<head>
<meta charset="utf-8">
<title>Tidewater Fishery – Identity and Business Cards</title>
<link rel="stylesheet" href="https://fonts.googleapis.com/css2?family=Open+Sans:wght@400;600;700&display=swap">
<style>
  :root {
    --stage: #111111;
    --brand-blue: #1c4f8f;
    --brand-blue-deep: #173f73;
    --card-face: #e7e7e9;
    --wave-grey: #b9bcc2;
    --text-blue: #1d3f70;
    --white: #ffffff;
    --fish-silver: #aab1b3;
    --fish-dark: #4a5052;
    --fillet-orange: #f07a48;
    --fillet-light: #f5a27c;
    --ice: #eceef1;
  }
  * { box-sizing: border-box; margin: 0; padding: 0; }
  html, body {
    width: 1200px; height: 1000px; overflow: hidden;
    background: var(--stage);
    font-family: "Open Sans", Arial, sans-serif;
  }
  .canvas { position: relative; width: 1200px; height: 1000px; }

  .brand-mark {
    position: absolute; left: 0; top: 150px; width: 1200px;
    text-align: center;
    font-weight: 700; font-size: 62px; letter-spacing: -1px; line-height: 1.2;
    color: var(--brand-blue);
  }

  .card {
    position: absolute; top: 347px; width: 511px; height: 306px;
    border-radius: 14px; overflow: hidden;
    background: var(--card-face);
  }
  .card--front { left: 50px; }
  .card--back { left: 633px; }
  .card svg.card-art { position: absolute; inset: 0; }

  .card-logo {
    position: absolute; font-weight: 700; color: var(--brand-blue);
    letter-spacing: -0.5px; white-space: nowrap; line-height: 1.2;
  }
  .card--front .card-logo { left: 0; width: 511px; text-align: center; top: 36px; font-size: 46px; }
  .card--back .card-logo { left: 20px; top: 30px; font-size: 27px; }

  .fish-illustration {
    position: absolute; left: 48px; top: 128px; width: 408px; height: 134px;
    border-radius: 24px;
    background:
      radial-gradient(ellipse 60% 45% at 55% 50%, rgba(235,238,239,0.9), rgba(235,238,239,0) 70%),
      linear-gradient(180deg, var(--fish-dark) 0%, var(--fish-silver) 40%, var(--card-face) 100%);
    opacity: 0.85;
  }

  .web-address {
    position: absolute; left: 0; width: 511px; bottom: 6px;
    text-align: center; color: var(--white); font-weight: 700; font-size: 15px;
  }

  .holder-name {
    position: absolute; left: 19px; top: 128px;
    font-size: 28px; font-weight: 600; color: var(--text-blue);
  }
  .contact-list {
    position: absolute; left: 19px; top: 203px; list-style: none;
    font-size: 14.5px; line-height: 17px; color: var(--text-blue);
  }
  .contact-list li { display: flex; align-items: flex-start; gap: 5px; }
  .contact-list li.address { margin-top: 4px; }
  .contact-list svg { width: 12px; height: 12px; margin-top: 3px; flex: none; fill: var(--text-blue); }
</style>
</head>
<body>
<main class="canvas">

  <div class="brand-mark">Tidewater Fishery</div>

  <section class="card card--front" aria-label="Business card front">
    <div class="card-logo">Tidewater Fishery</div>
    <div class="fish-illustration" role="img" aria-label="Photo of a whole Atlantic salmon, silver with dark spots, facing right"></div>
    <svg class="card-art" viewBox="0 0 511 306" aria-hidden="true">
      <path d="M0,262 C70,240 120,278 190,256 S300,242 360,260 S460,246 511,258 L511,306 L0,306 Z" fill="var(--wave-grey)"/>
      <path d="M0,276 C60,258 115,292 175,270 S285,256 345,274 S455,260 511,272 L511,306 L0,306 Z" fill="var(--brand-blue-deep)"/>
    </svg>
    <div class="web-address">www.tidewaterfishery.com.au</div>
  </section>

  <section class="card card--back" aria-label="Business card back">
    <svg class="card-art" viewBox="0 0 511 306">
      <defs>
        <radialGradient id="filletTones" cx="0.62" cy="0.52" r="0.5">
          <stop offset="0" stop-color="var(--fillet-orange)"/>
          <stop offset="0.6" stop-color="var(--fillet-light)"/>
          <stop offset="1" stop-color="var(--ice)"/>
        </radialGradient>
      </defs>
      <path d="M340,0 Q195,153 322,306 L511,306 L511,0 Z" fill="var(--brand-blue-deep)"/>
      <path d="M352,0 Q213,153 336,306 L511,306 L511,0 Z" fill="#8e9297"/>
      <path d="M362,0 Q228,153 348,306 L511,306 L511,0 Z" fill="url(#filletTones)" role="img" aria-label="Photo of two fresh salmon fillets resting on crushed ice"/>
    </svg>
    <div class="card-logo">Tidewater Fishery</div>
    <div class="holder-name">Liam Harper</div>
    <ul class="contact-list">
      <li><svg viewBox="0 0 12 12"><path d="M1,4 Q6,0 11,4 L9,5.5 L8,4 L4,4 L3,5.5 Z M2.5,6.5 L9.5,6.5 L10.5,11 L1.5,11 Z"/></svg>555-018-274</li>
      <li><svg viewBox="0 0 12 12"><path d="M3,0 H9 V12 H3 Z M4,1.5 V9 H8 V1.5 Z"/></svg>555-018-274</li>
      <li><svg viewBox="0 0 12 12"><path d="M0,2 H12 V10 H0 Z M1,3 L6,7 L11,3 Z"/></svg>tidewaterfishery@mail.com</li>
      <li class="address"><svg viewBox="0 0 12 12"><path d="M6,0 A4,4 0 0 1 10,4 C10,7 6,12 6,12 C6,12 2,7 2,4 A4,4 0 0 1 6,0 Z M6,2.5 A1.5,1.5 0 1 0 6,5.5 A1.5,1.5 0 1 0 6,2.5 Z"/></svg><span>7/210-238 Kellaway Rd<br>Coolum Bay 4573</span></li>
    </ul>
  </section>

</main>
</body>
</html>
```